Produktetikett für Mikronährstoffe
Wir sind sehr zufrieden und schätzen die schnelle Umsetzung von Änderungswünschen. Herzlichen Dank an Wilmaru
Zielgruppe
Herstellung und Vertrieb von Desinfektionsmitteln und jetz neu Mikronährstoffe. Und darum geht es. Wir möchten ein Etikett gestalten lassen das modern ist und trotzdem unsere Firmenfarben und unser Logo (evtl. stilisiert) enthält. Wahrscheinlich werden wir eine braune Flasche (ähnl. Apothekerflaschen) wählen.
Aufgabenstellung
Produktetikett für Mikronährstoffe (im Nahrungsergänzungsbereich) Die Ausführung der Flasche ist noch nicht bekannnt, jedoch schwebt uns eine braune oder dunkelgrüne Flasche vor. Auch gibt es noch keinen Namen für das Produkt.

```html
<!DOCTYPE html>
<html lang="de">
<head>
<meta charset="utf-8">
<title>VELMARO – Kraft am Morgen – Produktetikett</title>
<link rel="stylesheet" href="https://fonts.googleapis.com/css2?family=Montserrat:wght@400;500;600;700&display=swap">
<style>
  :root {
    --canvas-bg: #f4f4f2;
    --label-bg: #ffffff;
    --label-edge: #e2e6da;
    --brand-green: #9cc11f;
    --brand-teal: #1b9dc4;
    --text-teal: #1f9fc0;
    --veg-orange: #e8843a;
    --veg-green: #7fa84a;
    --veg-cream: #f3ead6;
  }
  * { box-sizing: border-box; margin: 0; padding: 0; }
  html, body {
    width: 1200px;
    height: 1200px;
    overflow: hidden;
    background: var(--canvas-bg);
    font-family: "Montserrat", Arial, sans-serif;
  }
  .canvas {
    position: relative;
    width: 1200px;
    height: 1200px;
  }
  .label {
    position: absolute;
    left: 250px;
    top: 150px;
    width: 700px;
    height: 900px;
    background: var(--label-bg);
    border: 1px solid var(--label-edge);
    box-shadow: 0 10px 30px rgba(0,0,0,0.08);
    overflow: hidden;
  }
  .brand-name {
    position: absolute;
    left: 200px;
    top: 52px;
    font-weight: 600;
    font-size: 48px;
    letter-spacing: 1px;
    color: var(--brand-teal);
  }
  .product-title {
    position: absolute;
    left: 0;
    right: 0;
    top: 238px;
    text-align: center;
    font-weight: 500;
    font-size: 64px;
    line-height: 1.1;
    color: var(--brand-green);
  }
  .headline {
    position: absolute;
    left: 0;
    right: 0;
    top: 372px;
    text-align: center;
    font-weight: 700;
    font-size: 30px;
    letter-spacing: 0.3px;
    color: var(--text-teal);
  }
  .description {
    position: absolute;
    left: 90px;
    right: 60px;
    top: 425px;
    text-align: center;
    font-weight: 500;
    font-size: 20px;
    line-height: 1.3;
    color: var(--text-teal);
  }
  .produce-illustration {
    position: absolute;
    left: 195px;
    right: 0;
    top: 590px;
    bottom: 0;
    background:
      radial-gradient(ellipse at 30% 65%, rgba(232,132,58,0.75), transparent 55%),
      radial-gradient(ellipse at 65% 40%, rgba(127,168,74,0.7), transparent 60%),
      radial-gradient(ellipse at 85% 75%, rgba(120,60,110,0.45), transparent 45%),
      linear-gradient(180deg, var(--veg-cream), #e6dcc4);
    border-radius: 40% 30% 0 0 / 30% 20% 0 0;
  }
  .ingredient-badge {
    position: absolute;
    left: 20px;
    top: 640px;
    width: 170px;
    height: 170px;
    border: 3px solid var(--brand-green);
    border-radius: 50%;
    background: var(--label-bg);
    display: flex;
    flex-direction: column;
    align-items: center;
    justify-content: center;
    text-align: center;
    color: var(--brand-green);
    font-weight: 500;
    font-size: 15px;
    line-height: 1.15;
  }
  .ingredient-badge .count {
    font-weight: 700;
    font-size: 46px;
    line-height: 1;
  }
</style>
</head>
<body>
<main class="canvas">
  <section class="label">
    <div class="brand-name">VELMARO</div>

    <h1 class="product-title">Kraft am Morgen</h1>

    <h2 class="headline">DAS VITALSTOFFKONZENTRAT</h2>
    <p class="description">Aus Früchten, Gemüse, Kräutern und Pflanzenölen – angereichert mit wichtigen Vitaminen und Mineralstoffen nach neuesten Erkenntnissen.</p>

    <div class="produce-illustration" role="img" aria-label="Aquarell-Illustration von Gemüse: Karotte, Spargel, Kohl, Paprika, Kürbis, Spinat, Aubergine, Avocado und Zucchiniblüte"></div>

    <div class="ingredient-badge">
      <span>Aus</span>
      <span class="count">70</span>
      <span>reinen<br>Zutaten</span>
    </div>
  </section>
</main>
</body>
</html>
```